Flaschenhalskarte für Weihnachten
korkwerk
Hat alles super geklappt - die Entscheidung für ein Design war schwer.
Zielgruppe
Wir beschäftigen uns mit dem Thema Wein und haben zur Informationen über Wein eine Flaschenhalskarte entwickelt. Diese Karte wollen wir nun Winzern und Händlern als Weihnachtsgrußkarte anbieten.
Aufgabenstellung
Es soll ein modernes und ansprechendes Design werden. Die Stanzlinien der Karte (Ausschnitt für den Flaschenhals und abfallender Rand) müssen berücksichtigt werden. Es können 2 Varianten angeboten werden - einmal die die ganze Länge, die Karte wird dann umgeklappt. Einmal nur bis zur Stanzlinie in der Mitte.
Die bisherigen Varianten der Karte findet man unter
http://korkanhaenger-muster.de/private-geniesser.html
Es dürfen auch Vorschläge für die Verpackung (einzeln und 10 Karten) gemacht werden.

```html
<!DOCTYPE html>
<html lang="de">
<head>
<meta charset="utf-8">
<title>Flaschenhalskarte Weihnachten – korkwerk</title>
<link rel="stylesheet" href="https://fonts.googleapis.com/css2?family=Cinzel:wght@400&family=Cabin+Condensed:wght@400&display=swap">
<style>
  :root {
    --paper: #ffffff;
    --green-top: #7a9452;
    --green-mid: #2f6a4d;
    --teal-bottom: #0c4652;
    --gold-light: #f6dc6a;
    --gold: #e2ae22;
    --gold-deep: #b37a12;
    --copper: #e39a3a;
    --die-line: #1c1c1c;
    --text-light: #ffffff;
  }
  html, body {
    margin: 0;
    padding: 0;
    width: 1200px;
    height: 4500px;
    overflow: hidden;
    background: var(--paper);
  }
  .canvas {
    position: relative;
    width: 1200px;
    height: 4500px;
  }
  .card-art {
    position: absolute;
    inset: 0;
    width: 1200px;
    height: 4500px;
  }
  .greeting {
    position: absolute;
    inset: 0;
    margin: 0;
    color: var(--text-light);
    font-family: "Cinzel", "Times New Roman", serif;
    font-weight: 400;
    line-height: 1;
  }
  .greeting-line {
    position: absolute;
    left: 51px;
    width: 1080px;
    text-align: center;
    display: block;
  }
  .greeting-frohe { font-size: 132px; top: 1648px; }
  .greeting-weihnachten { font-size: 96px; top: 1806px; }
  .greeting-und { font-size: 60px; top: 1976px; }
  .greeting-glueck { font-size: 98px; top: 2112px; }
  .greeting-jahr { font-size: 98px; top: 2204px; }
  .quote {
    position: absolute;
    left: 51px;
    width: 1080px;
    top: 3210px;
    margin: 0;
    text-align: center;
    color: var(--text-light);
    font-family: "Cabin Condensed", "Arial Narrow", sans-serif;
    font-size: 53px;
    line-height: 88px;
  }
  .quote-author {
    position: absolute;
    left: 51px;
    width: 1080px;
    top: 3626px;
    margin: 0;
    text-align: center;
    color: var(--text-light);
    font-family: "Cabin Condensed", "Arial Narrow", sans-serif;
    font-size: 44px;
  }
</style>
</head>
<body>
<div class="canvas">
  <svg class="card-art" viewBox="0 0 1200 4500" xmlns="http://www.w3.org/2000/svg">
    <defs>
      <linearGradient id="card-bg" x1="0" y1="0" x2="0" y2="1">
        <stop offset="0" stop-color="var(--green-top)"/>
        <stop offset="0.35" stop-color="var(--green-mid)"/>
        <stop offset="1" stop-color="var(--teal-bottom)"/>
      </linearGradient>
      <radialGradient id="bokeh-glow" cx="0.5" cy="0.5" r="0.5">
        <stop offset="0" stop-color="#c9dd9a" stop-opacity="0.3"/>
        <stop offset="1" stop-color="#c9dd9a" stop-opacity="0"/>
      </radialGradient>
      <linearGradient id="gold-area" x1="0" y1="0" x2="0" y2="1">
        <stop offset="0" stop-color="var(--gold-light)" stop-opacity="0.85"/>
        <stop offset="1" stop-color="var(--gold-deep)" stop-opacity="0.85"/>
      </linearGradient>
      <linearGradient id="copper-area" x1="0" y1="0" x2="0" y2="1">
        <stop offset="0" stop-color="var(--copper)" stop-opacity="0.35"/>
        <stop offset="1" stop-color="var(--copper)" stop-opacity="0.2"/>
      </linearGradient>
      <clipPath id="card-shape">
        <path d="M51,51 H1131 V4296 H990 A25,25 0 0 1 960,4331 Q860,4345 760,4390 Q590,4462 420,4390 Q320,4345 225,4331 A25,25 0 0 1 195,4296 H51 Z"/>
      </clipPath>
    </defs>

    <g clip-path="url(#card-shape)">
      <rect class="card-background" x="0" y="0" width="1200" height="4500" fill="url(#card-bg)"/>

      <g class="background-glow">
        <circle cx="380" cy="400" r="420" fill="url(#bokeh-glow)"/>
        <circle cx="950" cy="1050" r="380" fill="url(#bokeh-glow)"/>
        <circle cx="720" cy="2250" r="420" fill="url(#bokeh-glow)"/>
        <circle cx="300" cy="2950" r="330" fill="url(#bokeh-glow)" opacity="0.6"/>
        <circle cx="900" cy="3400" r="360" fill="url(#bokeh-glow)" opacity="0.5"/>
      </g>

      <rect class="illustration-area" role="img" aria-label="Goldene Weihnachtskugel mit Sternornament an einem Faden, oben rechts" x="621" y="51" width="489" height="699" rx="30" fill="url(#gold-area)"/>
      <rect class="illustration-area" role="img" aria-label="Goldene Weihnachtskugel mit Sternornament an einem Faden, links" x="51" y="51" width="405" height="1584" rx="30" fill="url(#gold-area)" opacity="0.35"/>
      <rect class="illustration-area" role="img" aria-label="Goldene Weihnachtskugel mit Sternornament an einem langen Faden, unten rechts" x="840" y="3510" width="291" height="585" rx="30" fill="url(#gold-area)"/>

      <rect class="illustration-area" role="img" aria-label="Kupferfarbene Schneeflocke, rechter Rand" x="870" y="1080" width="261" height="630" rx="24" fill="url(#copper-area)"/>
      <rect class="illustration-area" role="img" aria-label="Kupferfarbene Schneeflocke, linker Rand" x="51" y="2250" width="354" height="555" rx="24" fill="url(#copper-area)"/>
      <rect class="illustration-area" role="img" aria-label="Kupferfarbene Schneeflocke, unten links" x="51" y="4050" width="474" height="300" rx="24" fill="url(#copper-area)"/>

      <line class="fold-line" x1="51" y1="2736" x2="1131" y2="2736" stroke="var(--die-line)" stroke-width="2" opacity="0.5"/>
    </g>

    <path class="neck-die-cut" fill="none" stroke="var(--die-line)" stroke-width="3"
      d="M290,1180 C262,1160 262,1120 292,1110 C315,1104 318,1080 300,1040 C275,980 266,900 286,820 C300,760 305,710 340,690 C330,640 350,600 380,560 C420,510 470,470 540,455 C620,440 700,450 744,458 C800,470 820,520 850,560 C880,600 880,650 905,690 C930,740 900,800 912,860 C925,930 900,1000 905,1060 C910,1120 930,1170 905,1185 C880,1200 870,1175 886,1160"/>
  </svg>

  <h1 class="greeting">
    <span class="greeting-line greeting-frohe">Frohe</span>
    <span class="greeting-line greeting-weihnachten">Weihnachten</span>
    <span class="greeting-line greeting-und">und ein</span>
    <span class="greeting-line greeting-glueck">Glückliches</span>
    <span class="greeting-line greeting-jahr">neues Jahr</span>
  </h1>

  <p class="quote">Die Geburt Jesu in Bethlehem ist<br>keine einmalige Geschichte, sondern<br>ein Geschenk, das immer bleibt.</p>
  <p class="quote-author">Maria Lindner</p>
</div>
</body>
</html>
```